PREMIUM AGENCY High End Business Card - A+++ Designers Wanted

** DO NOT ATTEMPT TO CONTACT ME THROUGH SEARCHING ON ZINTREL OR EMAILING ME THROUGH MY WEBSITE **

I need a fresh, contemporary business card designed using the logo attached (BRONSALK)

I have attached the font for BRONSALK

It must have a premium look and feel. The business card size must be STANDARD size.

You can submit either/both VERTICAL or HORIZONTAL designs.

FRONT: It must have the following sample information on

Paul Ardley
Director Operations
Mobile +61 452 118 906
Email paulardley@bronsalk.com
www.bronsalk.com

The REAR of the business card must have the words

CREATE INSPIRE TOMORROW

as part of the design, in the same font (NEXA) attached.

The words do not need to be in capitals, or on the same line, please design this as you see it best working.

ADDITIONAL INFORMATION
======================

The BRONSALK logo must be on the front of the card

I want Ultraviolet printing on the final design, to enhance either the NAME of the person OR the BRONSALK logo OR the words on the back of the card.

Target Market(s)

Agency, Advertising Agency, Creative, Designers

Industry/Entity Type

Media

Contact Information for Business Card

Design Agency, Contemporary, Premium look and feel, High Quality

Font styles to use
Serif
Sans Serif
Other font styles liked:
• ATTACHED TO PROJECT

Requirements
Must have
• BLACK & WHITE as the primary design, and if you feel there can be a highlighted colour, then this can be used.
• The Logo ICON attached is blue, this colour must not be changed.
• I have attached the partner brand BRONSALK MEDIA incase you need to manipulate the original files.
• ** DO NOT ATTEMPT TO CONTACT ME THROUGH SEARCHING ON ZINTREL OR EMAILING ME THROUGH MY WEBSITE **
Nice to have
• Must be Premium. I have attached some sample designs, that I like that would be a good inspiration for where this can be taken.
• My favourite design is is the KESTRAVUE2-BUSINESSCARD-TEMPLATE
Should not have
• No funny or silly standard / off the shelf designs

```html
<!DOCTYPE html>
<html lang="en">
<head>
<meta charset="utf-8">
<title>Bronsalk Media Business Card</title>
<link rel="stylesheet" href="https://fonts.googleapis.com/css2?family=Montserrat:wght@300;500;800&family=Open+Sans:wght@400;600&display=swap">
<style>
  :root {
    --stage: #e9ebee;
    --brand-blue: #1f8fd6;
    --deep-blue: #0f63b8;
    --sky-blue: #6fd0f0;
    --aqua: #22c6e6;
    --ink: #3a3a3c;
    --paper: #ffffff;
    --paper-shade: #f1f2f4;
  }
  * { box-sizing: border-box; margin: 0; padding: 0; }
  html, body { width: 1200px; height: 1200px; overflow: hidden; }
  body { background: var(--stage); position: relative; font-family: "Open Sans", sans-serif; }

  .card {
    position: absolute; left: 150px; width: 900px; height: 514px;
    border-radius: 22px; overflow: hidden;
    box-shadow: 0 10px 30px rgba(0,0,0,0.18);
  }

  /* Rear */
  .card-back { top: 50px; }
  .back-pattern {
    position: absolute; inset: 0;
    background: radial-gradient(ellipse at 50% 55%, var(--sky-blue) 0%, #3db4ea 45%, var(--brand-blue) 100%);
  }
  .tagline {
    position: absolute; inset: 0; display: flex; flex-direction: column;
    align-items: center; justify-content: center;
    font-family: "Montserrat", sans-serif; color: var(--paper); line-height: 1;
  }
  .tagline-create { font-weight: 300; font-size: 40px; letter-spacing: 3px; margin-left: 150px; }
  .tagline-inspire { font-weight: 800; font-size: 104px; letter-spacing: 2px; margin: 6px 0; }
  .tagline-tomorrow { font-weight: 800; font-size: 42px; letter-spacing: 4px; margin-left: 70px; }

  /* Front */
  .card-front {
    top: 636px;
    background: linear-gradient(160deg, var(--paper) 40%, var(--paper-shade) 100%);
  }
  .band-top {
    position: absolute; top: 0; left: 330px; width: 500px; height: 20px;
    border-radius: 0 0 16px 16px;
    background: linear-gradient(90deg, var(--sky-blue), var(--brand-blue));
  }
  .band-bottom {
    position: absolute; bottom: 0; left: 120px; width: 710px; height: 36px;
    border-radius: 18px 18px 0 0;
    background: linear-gradient(90deg, var(--brand-blue), var(--deep-blue));
  }
  .brand {
    position: absolute; top: 72px; left: 56px; display: flex; align-items: center; gap: 26px;
  }
  .brand-dot { width: 62px; height: 62px; border-radius: 50%; background: var(--brand-blue); }
  .brand-name {
    font-family: "Montserrat", sans-serif; font-weight: 500; font-size: 56px;
    letter-spacing: 9px; color: var(--ink); white-space: nowrap;
  }
  .person { position: absolute; top: 250px; left: 70px; }
  .person-name {
    font-family: "Montserrat", sans-serif; font-weight: 800; font-size: 50px;
    color: var(--brand-blue); letter-spacing: 1px; line-height: 1;
  }
  .person-role { margin-top: 10px; font-size: 22px; color: var(--ink); letter-spacing: 0.5px; }

  .contacts { position: absolute; top: 240px; left: 470px; display: flex; flex-direction: column; gap: 24px; }
  .contact {
    display: flex; align-items: center; gap: 18px;
    width: 380px; height: 54px; padding: 0 22px;
    border-radius: 27px 27px 27px 27px;
    background: linear-gradient(90deg, #4fb6ea, var(--brand-blue));
    color: var(--paper); font-weight: 600; font-size: 17px; letter-spacing: 0.5px;
  }
  .contact:nth-child(3) { background: linear-gradient(90deg, var(--brand-blue), var(--deep-blue)); }
  .contact svg { width: 30px; height: 30px; flex: none; }
</style>
</head>
<body>

<section class="card card-back">
  <div class="back-pattern" role="img" aria-label="Repeating brand icon pattern in aqua on a blue gradient"></div>
  <div class="tagline">
    <span class="tagline-create">CREATE</span>
    <span class="tagline-inspire">INSPIRE</span>
    <span class="tagline-tomorrow">TOMORROW</span>
  </div>
</section>

<section class="card card-front">
  <div class="band-top"></div>

  <div class="brand">
    <span class="brand-dot"></span>
    <span class="brand-name">BRONSALK MEDIA</span>
  </div>

  <div class="person">
    <div class="person-name">PAUL ARDLEY</div>
    <div class="person-role">DIRECTOR OPERATIONS</div>
  </div>

  <div class="contacts">
    <div class="contact">
      <svg viewBox="0 0 24 24" aria-hidden="true"><path fill="#0f4f8a" d="M6.6 10.8a15 15 0 0 0 6.6 6.6l2.2-2.2a1 1 0 0 1 1-.25 11.4 11.4 0 0 0 3.6.57 1 1 0 0 1 1 1V20a1 1 0 0 1-1 1A17 17 0 0 1 3 4a1 1 0 0 1 1-1h3.5a1 1 0 0 1 1 1c0 1.25.2 2.45.57 3.57a1 1 0 0 1-.25 1z"/></svg>
      <span>+61 452 118 906</span>
    </div>
    <div class="contact">
      <svg viewBox="0 0 24 24" aria-hidden="true"><rect x="2" y="5" width="20" height="14" rx="1.5" fill="none" stroke="#ffffff" stroke-width="1.8"/><path d="M2.5 6 12 13l9.5-7" fill="none" stroke="#ffffff" stroke-width="1.8"/></svg>
      <span>paulardley@bronsalk.com</span>
    </div>
    <div class="contact">
      <svg viewBox="0 0 24 24" aria-hidden="true"><g fill="none" stroke="#0b3f70" stroke-width="1.8"><circle cx="12" cy="12" r="9.5"/><ellipse cx="12" cy="12" rx="4.5" ry="9.5"/><path d="M2.5 12h19M4 7h16M4 17h16"/></g></svg>
      <span>www.bronsalk.com</span>
    </div>
  </div>

  <div class="band-bottom"></div>
</section>

</body>
</html>
```